Homepage Website Design for luxury picnic company

We need a homepage designed for a luxury picnic business to match our updated branding/logo which we're currently completing on ArtGatherly with another competition. Please see attached logo/colour example to use for now.

PLEASE NOTE: We are only after graphic design concepts as part of this competition. I will get another developer to actually code the website.

It is important that this website is very elegant/luxurious and stands out from a visual perspective. The images really need to match the content/sections also. The new branding colours are silver with a dark background. Please create the new website homepage to match these colours/branding.

Please create as many concepts as possible and then I will provide feedback from there

The website content including sections is here https://pages.velmoranote.com/doc/d/7kRtWq2mLp9XcVb4Hn8Js3Yd6Fg1Za5Qe0Uo2Ti/edit?mode=share

Images to use are located here https://vault.trenquilbox.com/vault/dirs/5HmQzR2-NcWy8Kp41-7VbLdTsXoeFj?mode=share and there is also lots of videos at this link which you can screenshot images out of if needed https://www.stashquarry.com/sh/k827trwm3hdz4/AACvnRt2Lm8WqPe5Xu9JdsYk?dl=0

Any questions please contact me

```html
<!DOCTYPE html>
<html lang="en">
<head>
<meta charset="utf-8">
<title>Silver Ridge Picnics — Home</title>
<link rel="stylesheet" href="https://fonts.googleapis.com/css2?family=Cormorant+Garamond:wght@400;500;600&family=Lato:wght@400;700&display=swap">
<style>
:root{
  --ink:#0b0e1a;
  --paper:#ffffff;
  --panel:#e3e3e3;
  --mist:#f4f4f4;
  --silver:#c9cbd1;
  --muted:#8d8d8d;
  --body:#3a3a3a;
  --line:#9a9a9a;
}
*{margin:0;padding:0;box-sizing:border-box}
html,body{width:1200px;height:4304px;overflow:hidden}
body{position:relative;background:var(--paper);font-family:"Lato",sans-serif;color:var(--body)}
.abs{position:absolute}
.band{position:absolute;left:0;width:1200px}
.band--dark{background:var(--ink)}
.band--mist{background:var(--mist)}
.rule{position:absolute;height:1px;width:74px;background:var(--line)}
.eyebrow{position:absolute;font-family:"Cormorant Garamond",serif;font-weight:400;font-size:20px;letter-spacing:7px;text-transform:uppercase;color:var(--muted)}
.on-dark .eyebrow{color:var(--silver)}
.copy{position:absolute;font-size:9.5px;line-height:22px}
.copy p+p{margin-top:22px}
.on-dark .copy{color:#e6e6ea}
.photo{position:absolute}
.btn{position:absolute;display:flex;align-items:center;justify-content:center;font-family:"Cormorant Garamond",serif;font-weight:600;font-size:12px;letter-spacing:1px;text-transform:uppercase;border:1px solid currentColor}
.on-dark .btn{color:#fff}
.list{position:absolute;list-style:none;font-size:9.5px;line-height:25.5px}
.list li{position:relative;padding-left:26px}
.list li::before{content:"";position:absolute;left:0;top:8px;width:7px;height:7px;background:currentColor;transform:rotate(45deg)}
.on-dark .list{color:#fff}
.display{position:absolute;font-family:"Cormorant Garamond",serif;font-weight:500;color:#fff}
.subhead{position:absolute;font-family:"Cormorant Garamond",serif;font-weight:400;font-size:18px;line-height:22px;text-transform:uppercase;color:var(--muted)}
.field{position:absolute;border:1px solid #555;font-family:"Cormorant Garamond",serif;font-weight:600;font-size:12px;letter-spacing:.5px;color:#555;padding:14px 14px}
.footer-head{position:absolute;font-family:"Cormorant Garamond",serif;font-weight:400;font-size:17px;letter-spacing:5px;color:var(--silver)}
.footer-links{position:absolute;list-style:none;font-family:"Cormorant Garamond",serif;font-size:12px;line-height:30px;color:#fff;font-weight:600}
.support-panel{z-index:1}
.support-photo{z-index:2}
.support-text{z-index:3}
</style>
</head>
<body>

<!-- Food & Beverages -->
<section class="band band--dark on-dark" style="top:0;height:548px">
  <div class="photo" role="img" aria-label="Gourmet picnic spread with berries, cheese board and chilled bottles on ice" style="left:112px;top:64px;width:301px;height:421px;background:linear-gradient(180deg,#a99aa6 0%,#d9d3d6 40%,#6b4a40 75%,#7a1420 100%)"></div>
  <span class="rule" style="left:500px;top:75px"></span>
  <h2 class="eyebrow" style="left:500px;top:92px">Food &amp; Beverages</h2>
  <div class="copy" style="left:500px;top:140px;width:590px">
    <p>Our delicious food and beverages will have your mouth watering regardless of your tastes or dietary requirements. Our Gourmet Picnic menu is fully customisable so you can design your own picnic. We cater for allergies, vegans, celiacs and all other dietary requirements. It is quick and easy to select your choices via our website which means it is no big deal if you do have specific requirements!</p>
    <p>We focus on offering a lot of diversity with the finest ingredients. We're a registered food business meaning we prepare, store and transport our food in accordance with all food handling guidelines. We have also put a lot of thought into the logistics of serving this food at our picnic locations and ensure the food is as refrigerated and fresh as possible. Each Gourmet Picnic includes the following:</p>
  </div>
  <ul class="list" style="left:500px;top:324px;width:260px">
    <li>2 Choices of Cheese, Dips or Antipasto</li>
    <li>2 Choices of Crackers</li>
    <li>Seasonal Fruit</li>
  </ul>
  <ul class="list" style="left:766px;top:324px;width:330px">
    <li>1 Choice of Nuts or Dried Fruit</li>
    <li>1 Choice of Chocolate</li>
    <li>2 Choices of Complimentary Beer, Wine or Non-Alcoholic Beverages</li>
  </ul>
  <a class="btn" style="left:500px;top:430px;width:262px;height:43px">View Menu</a>
</section>

<!-- Support Local -->
<section class="band" style="top:548px;height:525px"></section>
<div class="abs support-panel" style="left:486px;top:511px;width:600px;height:600px;background:var(--panel)"></div>
<span class="rule support-text" style="left:112px;top:623px"></span>
<h2 class="eyebrow support-text" style="left:112px;top:642px">Support Local</h2>
<div class="copy support-text" style="left:112px;top:692px;width:470px">
  <p>The Blue Mountains economy has been doing it tough with tourism taking a dramatic downturn after the bushfires in late 2019 and more recently COVID-19. We're a small business run by a young local couple who invest their passion and energy to make our picnics something special.</p>
  <p>We have a greater purpose than simply making money, Silver Ridge Picnics has been created to enable couples, families and friends to create special memories together in a truly unique way.</p>
  <p>We also have a team of locals who help us out on the weekends with delivering and setting up the picnics. By organising a picnic with us and simply visiting the Blue Mountains, you will be doing your part to help.</p>
</div>
<div class="photo support-photo" role="img" aria-label="Couple relaxing on cushions at a clifftop picnic" style="left:593px;top:625px;width:249px;height:374px;background:linear-gradient(180deg,#3d4a2c 0%,#5b5a48 45%,#2a2a33 75%,#7e2a30 100%)"></div>
<div class="photo support-photo" role="img" aria-label="Couple sharing a picnic on a rocky lookout above the valley" style="left:864px;top:668px;width:336px;height:301px;background:linear-gradient(180deg,#5a6272 0%,#3d4a3a 45%,#6a4a44 75%,#a9a4a0 100%)"></div>

<!-- Gift Certificates -->
<section class="band band--dark on-dark" style="top:1111px;height:438px">
  <span class="rule" style="left:112px;top:37px"></span>
  <h2 class="eyebrow" style="left:112px;top:55px">Gift Certificates</h2>
  <h3 class="display" style="left:112px;top:102px;width:490px;font-size:38px;line-height:54px">Do you struggle for gift ideas? Worried about wasting your money on something they won’t like?</h3>
  <p class="abs" style="left:112px;top:326px;width:490px;font-family:'Cormorant Garamond',serif;font-size:15px;letter-spacing:4px;line-height:18px;color:var(--silver)">Our picnics are a unique and memorable gift that everyone will love!</p>
  <div class="photo" role="img" aria-label="Gift voucher artwork with gold ribbon" style="left:637px;top:100px;width:449px;height:203px;background:linear-gradient(90deg,#f2f2f2 0%,#e4e4e4 50%,#d8b24a 100%)"></div>
</section>

<!-- Gift details -->
<section class="band" style="top:1549px;height:399px">
  <h4 class="subhead" style="left:112px;top:72px;width:400px">We can mail you a professionally printed gift certificate at no extra cost!</h4>
  <div class="copy" style="left:112px;top:150px;width:410px">
    <p>We make it super simple to organise an amazing gift for your friend or loved one. We have an online system to organise your Gift Certificate which takes less than 5 minutes.</p>
    <p>Once you have gifted it, the recipient follows the instructions on the certificate to choose their own location and date/time. If you choose the catered option they can also select all their own food and beverages once they have booked in.</p>
    <p>It's really as simple as that!</p>
  </div>
  <span class="abs" style="left:556px;top:80px;width:1px;height:230px;background:#e2e2e2"></span>
  <h4 class="subhead" style="left:592px;top:72px;width:420px">We also offer payment plans on gift certificates</h4>
  <div class="copy" style="left:592px;top:128px;width:494px">
    <p>You can pay off the Gift Certificate between when you book and need to gift the certificate. All we need is a $50 + GST deposit and then the remainder can be split up into weekly equal payments or any other payment arrangements you like.</p>
    <p>Best of all we do not charge any extra for this service.</p>
  </div>
  <a class="btn" style="left:592px;top:277px;width:262px;height:46px;color:var(--ink)">Organise Your Gift Certificate</a>
</section>

<!-- Picnic Setting -->
<section class="band band--dark on-dark" style="top:1948px;height:475px">
  <span class="rule" style="left:112px;top:74px"></span>
  <h2 class="eyebrow" style="left:112px;top:92px">Picnic Setting</h2>
  <h3 class="display" style="left:112px;top:138px;width:660px;font-size:38px;line-height:52px">Never gone on a proper picnic as it’s too much effort?</h3>
  <p class="abs" style="left:112px;top:256px;width:630px;font-family:'Cormorant Garamond',serif;font-size:15px;line-height:22px;color:#d8d8de">Let’s be honest, everyone loves picnics but no one loves buying the food, transporting everything, setting up and then having to clean and sort everything out the next day because you’re too exhausted to do it after the picnic.</p>
</section>
<div class="photo" role="img" aria-label="Picnic setup on a red persian rug with grazing board and ice bucket" style="left:319px;top:2309px;width:562px;height:373px;background:linear-gradient(180deg,#2c2c33 0%,#6a1c24 45%,#8a2a2c 70%,#b9b6b2 100%)"></div>
<p class="abs" style="left:336px;top:2712px;width:760px;font-family:'Cormorant Garamond',serif;font-size:15px;line-height:22px;color:var(--muted)">Included as part of every picnic is the hire of our picnic equipment including transport, setup, pack up and cleaning. Our picnic setting consists of</p>
<ul class="list" style="left:336px;top:2774px;width:320px;color:var(--ink)">
  <li style="color:var(--body)">2 persian rugs to replace a traditional picnic blanket</li>
  <li style="color:var(--body)">Lots of cushions so you're super comfy</li>
  <li style="color:var(--body)">Decor including flowers, candles, lantern and more</li>
  <li style="color:var(--body)">Picnic basket, blankets, games and a first aid kit</li>
</ul>
<ul class="list" style="left:664px;top:2774px;width:400px">
  <li>Bluetooth speaker so you can play your favourite music (or podcast!)</li>
  <li>Table to place drinks</li>
  <li>Ice bucket and glassware</li>
</ul>

<!-- COVID safe -->
<section class="band band--mist" style="top:2944px;height:189px;text-align:center">
  <h4 class="abs" style="left:0;width:1200px;top:30px;font-family:'Cormorant Garamond',serif;font-weight:500;font-size:14px;color:var(--ink)">WE’RE COVID SAFE</h4>
  <p class="abs" style="left:266px;width:668px;top:66px;font-family:'Cormorant Garamond',serif;font-size:15px;line-height:22px;color:var(--ink)">We are very conscious of everyone’s health and well being during these unprecedented times. You can have confidence knowing we’re a registered COVID safe business with the NSW Government. We follow all health protocols when setting up and preparing our picnics. If you want to know any further details or have any requests please just reach out.</p>
</section>

<!-- FAQ -->
<section class="band band--dark on-dark" style="top:3133px;height:234px">
  <h2 class="abs" style="left:0;width:1200px;top:68px;text-align:center;font-family:'Cormorant Garamond',serif;font-weight:500;font-size:20px;letter-spacing:7px;color:#fff">FREQUENTLY ASKED QUESTIONS</h2>
  <a class="btn" style="left:445px;top:114px;width:262px;height:45px">Go to FAQ</a>
</section>

<!-- Contact -->
<section class="band" style="top:3367px;height:577px">
  <span class="rule" style="left:112px;top:74px"></span>
  <h2 class="eyebrow" style="left:112px;top:94px">Contact</h2>
  <div class="field" style="left:112px;top:149px;width:449px;height:44px">FIRST NAME</div>
  <div class="field" style="left:637px;top:149px;width:449px;height:44px">LAST NAME</div>
  <div class="field" style="left:112px;top:209px;width:449px;height:44px">EMAIL</div>
  <div class="field" style="left:637px;top:209px;width:449px;height:44px">PHONE NUMBER</div>
  <div class="field" style="left:112px;top:269px;width:974px;height:149px">EMAIL</div>
  <a class="btn" style="left:468px;top:455px;width:262px;height:45px;background:var(--ink);color:#fff;border-color:var(--ink)">Submit</a>
</section>

<!-- Footer -->
<footer class="band band--dark" style="top:3944px;height:360px">
  <h3 class="footer-head" style="left:112px;top:70px">QUICK MENU</h3>
  <ul class="footer-links" style="left:112px;top:98px">
    <li>Pricing</li><li>Picnic Spots</li><li>Food &amp; Beverages</li><li>Gift Certificates</li>
  </ul>
  <h3 class="footer-head" style="left:483px;top:70px">INFORMATION</h3>
  <ul class="footer-links" style="left:483px;top:98px">
    <li>FAQs</li><li>About</li>
  </ul>
  <h3 class="footer-head" style="left:854px;top:70px">CONTACT DETAILS</h3>
  <p class="abs" style="left:854px;top:106px;width:215px;font-family:'Cormorant Garamond',serif;font-weight:600;font-size:12px;line-height:15px;color:#fff">PO Box 7314 Ferncliff NSW 2790, 02 5550 1847</p>
  <p class="abs" style="left:854px;top:150px;font-family:'Cormorant Garamond',serif;font-weight:600;font-size:12px;color:#fff">info@silverridgepicnics.com.au</p>
  <span class="abs" style="left:112px;top:250px;width:974px;height:1px;background:#4a4d5a"></span>
  <p class="abs" style="left:112px;top:270px;font-family:'Cormorant Garamond',serif;font-weight:600;font-size:12px;color:#fff">Copyright © 2020, Silver Ridge Picnics, All Rights Reserved</p>
  <p class="abs" style="left:846px;top:270px;font-family:'Cormorant Garamond',serif;font-weight:600;font-size:12px;color:#fff">Privacy Policy <span style="margin:0 26px;color:#888">|</span> Terms &amp; Conditions</p>
</footer>

</body>
</html>
```